■依頼の目的/概要
ベストセラー作家が送る最新作の表紙を飾りませんか?
Borelo QuillのBWSの電子書籍表紙デザインをお願いします。

■本の内容
*タイトル:
うつむく朝に灯すひと匙の言葉

というタイトルの表紙デザインの発注になります。

■デザイン要望

要望1つ目
作家名は後でお伝えします。作家名もどこかに挿入いただきたいです。よろしくお願いします。
提出の際は ○○著という形でご提出よろしくお願いします。

要望2つ目
ウェルネスバランスコーチ検定資格保持者

とどこかに入れてください。

要望3つ目
累計Borelo 1位〇冠
(現在、59冠までいっています。今後、出版が控えている作品があります。
そのため、その最終冠数を入れて頂きたいです。)

とどこかに入れてください。

また、出来上がったデザインを作家グループの中で投票にかけて、
一番投票得票数の多かったものを表紙デザインとして選ばせていただきたいと考えております。
もしかしたら、その中で、何か修正依頼など来るかもしれませんが、
それも含めて、ご対応していただける方よろしくお願いします。

また、最終、選考後、
累計Borelo 1位〇〇冠   と記載された表紙と、
累計Borelo 1位〇〇冠   と記載されない表紙の
2表紙の納品をよろしくお願いします。他の部分の表紙のデザイン変更は不要です。
(これは、最終選ばれたデザイナーさんのみご対応で大丈夫です。)

お手数をおかけしますが、よろしくお願いします。

1部内容の抜粋を記載します。

データサイズですが、推奨サイズでJPEGファイルでご納品下さい、よろしくお願いします。
(推奨サイズは2560×1600pxです。)
その他何かご不明な点がございましたら、お気軽にご質問下さい。
よろしくお願いいたします。
変更点がでてきました。

累計Borelo 1位〇〇冠→累計Borelo 1位65冠
と決定しました。最終、この数字でご納品ください。

もうすでに提出済みの方に関しましては、当選後のご対応で大丈夫です。
お手数をおかけしますが、ご対応なにとぞよろしくお願いいたします。
皆様、たくさんのご応募まことにありがとうございました。
コンペというとても厳しい条件にも関わらず、挑戦いただいたことに
大変大変感謝しております。
ご提案されましたすべての作品、デザイナー様のご経歴、作成への思い入れ、
すべてを拝見させていただきました。
これから、作家グループへ全体回覧のメールを致します。
作家グループの皆様の投票結果までお待ちください(場合により結果
公表まで1週間から10日ぐらいかかる場合もあると思われます)。
また、この度、いろいろな作品に触れさせていただきましたこと本当に
本当に感謝いたします。
皆さまのご努力、精進そしてそのチャレンジに大変感謝と尊敬を感じております。
ご経歴やデザイナー様の名前などすべて伏せて、作品のみの提示にて
小説家作家グループに提案させていただきたいと思っております。
ただ、今回の表紙に関しましては、どうしても1名しか選べない状況がございますこと
また、総選挙による投票にて決定致しますこと、ご理解何卒よろしくお願い申しあげます。
また、もしも、今回当選に至らないことがありましても、
今後も私自身は作家生活を継続予定ですので、
(今回は作品の表紙に合わないことがあっても)作風の気に入ったデザイナー様には
個人的にお話を相談させていただく場合もあると思っております。
また、別の作品の表紙を飾っていただく可能性もあるかと思っております。
この度は誠に誠にありがとうございました。
表紙ですが、最終選考決定いたしました。
当選された方には個別に連絡をさせていただきました。

皆様からのご提案、そして、そのチャレンジに敬意と感謝をしております。
私はこれからも作家活動を継続致しますので、また、ご一緒にお仕事をさせていただき
表紙を飾っていただく機会もあるかと思います。
その際はなにとぞよろしくお願いもうしあげます。
自分のためだけでなく、ベストセラーを取り続けることで、素晴らしい表紙を飾れるチャンスをこれからも作りたいと思い、また、精進していきたいと思います。
この度はまことにありがとうございました。

「目が惹きつけられました」とか
これから上を向いて、光を見て行こうとする視線と深く、それでいて爽やかなブルーのタッチがとても印象的で綺麗‼️
など目が離せない、というようなコメントを多くいただきました。
ご提出誠にありがとうございます。

コンペについてはとても厳しい条件にも関わらず挑戦していただき、
本当に一つのタイトルに対する皆様の創造力について驚きや才能についてをいつも
感じています。
そして、そのチャレンジする姿勢にいつもエネルギーをいただき、
私自身もこれからも、いろいろなことに挑戦する姿勢を続けていきたいな、
と感じております。
表紙を飾っていただく機会もあるかと思います。
その際はなにとぞよろしくお願いもうしあげます。この度はありがとうございました。

```html
<!DOCTYPE html>
<html lang="ja">
<head>
<meta charset="utf-8">
<title>うつむく朝に灯すひと匙の言葉 — 表紙</title>
<link rel="stylesheet" href="https://fonts.googleapis.com/css2?family=M+PLUS+Rounded+1c:wght@800&family=Noto+Sans+JP:wght@700;900&family=Noto+Serif+JP:wght@700;900&display=swap">
<style>
  :root {
    --frame: #a195d0;
    --paper: #ffffff;
    --banner: #3aa99c;
    --banner-text: #ffffff;
    --title: #4a4a4a;
    --ink: #2b2b2b;
    --figure-light: #ffffff;
    --figure-mid: #ececec;
    --figure-edge: #b9b9b9;
    --ground-shade: #c9c9c9;
    --badge-gold-light: #ead58f;
    --badge-gold: #b38b32;
  }
  * { margin: 0; padding: 0; box-sizing: border-box; }
  html, body {
    width: 750px; height: 1200px; overflow: hidden;
    background: var(--frame);
  }
  .cover {
    position: relative;
    width: 750px; height: 1200px;
    background: var(--frame);
    font-family: "Noto Sans JP", sans-serif;
  }
  .cover__page {
    position: absolute;
    left: 25px; top: 20px;
    width: 700px; height: 1160px;
    background: var(--paper);
    overflow: hidden;
  }
  .subtitle-banner {
    position: absolute;
    left: 100px; top: 2px;
    width: 500px; height: 64px;
    background: var(--banner);
    border-radius: 32px;
    color: var(--banner-text);
    font-family: "M PLUS Rounded 1c", "Noto Sans JP", sans-serif;
    font-weight: 800;
    font-size: 40px;
    line-height: 64px;
    text-align: center;
    letter-spacing: 0.04em;
  }
  .title {
    position: absolute;
    left: 0; top: 0;
    width: 700px;
    color: var(--title);
    font-family: "Noto Sans JP", sans-serif;
    font-weight: 900;
  }
  .title__line {
    position: absolute;
    left: 0; width: 700px;
    display: block;
    text-align: center;
    white-space: nowrap;
  }
  .title__line--top { top: 150px; font-size: 158px; line-height: 180px; }
  .title__line--bottom { top: 360px; font-size: 188px; line-height: 210px; letter-spacing: 0.06em; }
  .figure-ground {
    position: absolute;
    left: 150px; top: 930px;
    width: 330px; height: 90px;
    border-radius: 50%;
    background: radial-gradient(ellipse at 50% 50%, var(--ground-shade) 0%, rgba(201,201,201,0.5) 45%, rgba(255,255,255,0) 72%);
  }
  .figure-art {
    position: absolute;
    left: 215px; top: 585px;
    width: 290px; height: 405px;
    border-radius: 48% 48% 44% 44% / 38% 38% 62% 62%;
    background:
      radial-gradient(ellipse at 42% 30%, var(--figure-light) 0%, var(--figure-light) 35%, var(--figure-mid) 70%, #d6d6d6 100%);
    box-shadow: inset 0 0 0 4px var(--figure-edge), inset -18px -22px 40px rgba(0,0,0,0.06);
  }
  .credential {
    position: absolute;
    left: 36px; top: 1042px;
    font-weight: 700;
    font-size: 20px;
    color: var(--ink);
    letter-spacing: 0.01em;
    white-space: nowrap;
  }
  .author {
    position: absolute;
    left: 36px; top: 1082px;
    display: flex; align-items: center; gap: 40px;
    color: var(--ink);
  }
  .author__label { font-size: 44px; font-weight: 900; }
  .author__name { font-size: 42px; font-weight: 700; letter-spacing: 0.04em; }
  .award {
    position: absolute;
    left: 478px; top: 935px;
    width: 200px; height: 210px;
  }
  .award__wreath {
    position: absolute; inset: 0;
    border-radius: 50%;
    background: radial-gradient(ellipse at 50% 50%, rgba(255,255,255,0) 55%, var(--badge-gold-light) 60%, var(--badge-gold) 68%, rgba(255,255,255,0) 71%);
  }
  .award__text {
    position: absolute; inset: 0;
    display: flex; flex-direction: column; align-items: center; justify-content: center;
    color: var(--ink);
    font-family: "Noto Serif JP", serif;
    font-weight: 700;
    line-height: 1.15;
  }
  .award__label { font-family: "Noto Sans JP", sans-serif; font-size: 16px; }
  .award__rank { font-family: "Noto Sans JP", sans-serif; font-size: 16px; margin-top: 2px; }
  .award__count { font-size: 40px; font-weight: 900; }
</style>
</head>
<body>
<main class="cover">
  <section class="cover__page">
    <div class="subtitle-banner">うつむく朝に灯す</div>
    <h1 class="title">
      <span class="title__line title__line--top">ひと匙の</span>
      <span class="title__line title__line--bottom">言葉</span>
    </h1>
    <div class="figure-ground"></div>
    <div class="figure-art" role="img" aria-label="うつむいて膝を抱えて座る白い人型キャラクターのイラスト"></div>
    <p class="credential">ウェルネスバランスコーチ検定資格保持者</p>
    <p class="author">
      <span class="author__label">著者</span>
      <span class="author__name">○○</span>
      <span class="author__name">○○</span>
    </p>
    <div class="award">
      <div class="award__wreath" role="img" aria-label="金色の月桂冠の飾り"></div>
      <div class="award__text">
        <span class="award__label">累計 Borelo</span>
        <span class="award__rank">1位</span>
        <span class="award__count">65冠</span>
      </div>
    </div>
  </section>
</main>
</body>
</html>
```